A world class design for a " Discount services provider"
Brightfold Savings Network International
A world class design for a " Discount services provider" - Financial Services
Creative Brief
Simple
Kemi ARUBA
Managing Partner
Suite 204, 306 & 118, Corlenne Plaza, Opp. Former Harbour Works Bureau, Tesvara Crescent , Zone 8, Ilumo Abuja - FCT
infokemiaruba@brightfoldmail.example
www.brightfoldsavingsnet.example
The back of the business card should carry my detailed imformation, while the front should carry only the company's designed logo and colour.
Tavolin Tavolin
Dear Designers, Thank you for the wonderful work you have submitted so far. Looking forward to see more beautiful and creative designs though. Great minds!
Dear Designers, Please remember that I also need the following Stationary designs in addtion to the business card design. 1. Letterhead (A4 Size 210mm x 297mm) 2. Envelope (C4 Size 229mmx324mm) 3. Email Signature

```html
<!DOCTYPE html>
<html lang="en">
<head>
<meta charset="utf-8">
<title>Brightfold Savings Network International — Business Card</title>
<link rel="stylesheet" href="https://fonts.googleapis.com/css2?family=Exo+2:ital,wght@0,400;0,500;0,600;1,400&display=swap">
<style>
  :root {
    --bg: #e9e9eb;
    --card-white: #ffffff;
    --card-grey: #e4e5e8;
    --brand-blue: #1f63c9;
    --brand-blue-light: #3f86e6;
    --brand-blue-dark: #0f3f94;
    --ink: #1b1b1f;
    --on-blue: #ffffff;
    --shadow: rgba(20, 30, 50, 0.22);
  }
  * { margin: 0; padding: 0; box-sizing: border-box; }
  html, body { width: 1200px; height: 899px; overflow: hidden; }
  body {
    background: var(--bg);
    font-family: "Exo 2", "Helvetica Neue", Arial, sans-serif;
    position: relative;
  }
  .card {
    position: absolute;
    border-radius: 4px;
    overflow: hidden;
    box-shadow: 0 10px 28px var(--shadow);
  }
  /* Front */
  .card-front {
    left: 560px; top: 70px;
    width: 560px; height: 320px;
    background: var(--card-white);
    display: flex; align-items: center; justify-content: center;
  }
  .brand {
    display: flex; align-items: center; gap: 12px;
    color: var(--brand-blue);
    font-weight: 500;
    text-transform: uppercase;
    letter-spacing: 0.5px;
  }
  .brand-dot {
    flex: none;
    border-radius: 50%;
    background: var(--brand-blue);
  }
  .card-front .brand { font-size: 17px; }
  .card-front .brand-dot { width: 34px; height: 34px; }

  /* Back */
  .card-back {
    left: 80px; top: 460px;
    width: 640px; height: 366px;
    background: linear-gradient(180deg, var(--card-white) 0%, var(--card-grey) 55%);
  }
  .card-back .wave { position: absolute; inset: 0; width: 100%; height: 100%; }
  .card-back .brand {
    position: absolute; left: 28px; top: 38px;
    font-size: 13px;
  }
  .card-back .brand-dot { width: 28px; height: 28px; }
  .holder {
    position: absolute; right: 34px; top: 96px;
    text-align: right;
  }
  .holder-name {
    font-size: 24px; font-weight: 500;
    color: var(--brand-blue-dark);
    letter-spacing: 1.5px;
    text-transform: uppercase;
  }
  .holder-title {
    font-size: 16px; font-style: italic;
    color: var(--ink);
    margin-top: 2px;
  }
  .contacts {
    position: absolute; left: 30px; top: 198px;
    list-style: none;
    color: var(--on-blue);
    font-size: 12px;
  }
  .contacts li { display: flex; align-items: center; gap: 9px; height: 24px; }
  .contacts svg { width: 14px; height: 14px; flex: none; }
  .address {
    position: absolute; right: 34px; top: 262px;
    text-align: right;
    color: var(--on-blue);
    font-size: 13px; line-height: 1.45;
  }
  .website {
    position: absolute; right: 34px; top: 318px;
    color: var(--on-blue);
    font-size: 14px;
    letter-spacing: 0.3px;
  }
</style>
</head>
<body>

<section class="card card-front" aria-label="Business card front">
  <div class="brand">
    <span class="brand-dot"></span>
    <span class="brand-name">Brightfold Savings Network International</span>
  </div>
</section>

<section class="card card-back" aria-label="Business card back">
  <svg class="wave" viewBox="0 0 640 366" preserveAspectRatio="none" aria-hidden="true">
    <defs>
      <linearGradient id="blueBand" x1="0" y1="0" x2="1" y2="1">
        <stop offset="0" stop-color="var(--brand-blue-dark)"/>
        <stop offset="0.45" stop-color="var(--brand-blue-light)"/>
        <stop offset="1" stop-color="var(--brand-blue)"/>
      </linearGradient>
    </defs>
    <path d="M0,164 C170,128 330,196 640,186 L640,366 L0,366 Z" fill="url(#blueBand)"/>
    <path d="M0,150 C170,112 330,180 640,170" fill="none" stroke="var(--ink)" stroke-width="6"/>
    <path d="M0,158 C170,121 330,189 640,179" fill="none" stroke="var(--card-white)" stroke-width="3"/>
  </svg>

  <div class="brand">
    <span class="brand-dot"></span>
    <span class="brand-name">Brightfold Savings Network International</span>
  </div>

  <div class="holder">
    <p class="holder-name">Kemi Aruba</p>
    <p class="holder-title">Managing Director</p>
  </div>

  <ul class="contacts">
    <li>
      <svg viewBox="0 0 16 16" aria-hidden="true"><path fill="currentColor" d="M3.6 1.5l2.3 2.6-1.2 1.8c.9 2 2.4 3.5 4.4 4.4l1.8-1.2 2.6 2.3-1.3 2.1C7.4 13.6 2.4 8.6 1.5 3.8z"/></svg>
      <span>012 555 0147</span>
    </li>
    <li>
      <svg viewBox="0 0 16 16" aria-hidden="true"><rect x="4.5" y="1" width="7" height="14" rx="1.3" fill="none" stroke="currentColor" stroke-width="1.5"/><circle cx="8" cy="12.5" r="0.9" fill="currentColor"/></svg>
      <span>012 555 0148</span>
    </li>
    <li>
      <svg viewBox="0 0 16 16" aria-hidden="true"><rect x="4" y="1.5" width="8" height="4" fill="currentColor"/><rect x="1.5" y="6" width="13" height="6" rx="1" fill="currentColor"/><rect x="4" y="10" width="8" height="4.5" fill="currentColor" stroke="var(--brand-blue)" stroke-width="0.8"/></svg>
      <span>012 555 0149</span>
    </li>
    <li>
      <svg viewBox="0 0 16 16" aria-hidden="true"><rect x="1.5" y="3.5" width="13" height="9" rx="1" fill="none" stroke="currentColor" stroke-width="1.4"/><path d="M1.8 4l6.2 5 6.2-5" fill="none" stroke="currentColor" stroke-width="1.4"/></svg>
      <span>infokemiaruba@brightfoldmail.example</span>
    </li>
  </ul>

  <p class="address">204 Corlenne Plaza, Tesvara Crescent<br>Ilumo</p>
  <p class="website">www.brightfoldsavingsnet.example</p>
</section>

</body>
</html>
```